Real Estate "For Sale" Sign for construction company

We need a sign that we can use to hang on a post and place on the road when we sell a property. The sign will be simple and will need to mainly feature our logo (files attached), as well as the words "For Sale", and then our phone number "(555) 617 3489". The sign will hang on a post that'll look something like the attached picture.

Target Market(s)

Home buyers

Industry/Entity Type

Real Estate

Font styles to use
Serif
Sans Serif

Colors
0054AA
0677BA
7BADD7
CADEEF
E8F1F8
0094D4
00A9DD
6FCCEA
C7EBF8
E9F6FB

Requirements
Must have
• For Sale & our phone number

```html
<!DOCTYPE html>
<html lang="en">
<head>
<meta charset="utf-8">
<title>For Sale Sign – Ridgeline Crest Realty</title>
<link rel="stylesheet" href="https://fonts.googleapis.com/css2?family=Anton&family=Red+Hat+Display:wght@500&display=swap">
<style>
  :root {
    --backdrop: #8a919b;
    --sign-white: #ffffff;
    --sky-blue: #40c8f4;
    --brand-blue: #1681c4;
    --deep-blue: #0a52a8;
    --navy: #131f4b;
  }
  html, body {
    margin: 0;
    width: 942px;
    height: 1200px;
    overflow: hidden;
    background: var(--backdrop);
  }
  .sign {
    position: absolute;
    left: 109px;
    top: 87px;
    width: 725px;
    height: 994px;
    background: var(--sign-white);
    overflow: hidden;
  }
  .brand-mark {
    position: absolute;
    left: 307px;
    top: 86px;
    width: 110px;
    height: 110px;
    border-radius: 50%;
    background: var(--brand-blue);
  }
  .brand-name {
    position: absolute;
    left: 0;
    right: 0;
    top: 196px;
    margin: 0;
    text-align: center;
    font-family: "Red Hat Display", sans-serif;
    font-weight: 500;
    color: var(--brand-blue);
    font-size: 60px;
    line-height: 1;
    letter-spacing: 1px;
  }
  .brand-name .brand-sub {
    display: block;
    font-size: 20px;
    letter-spacing: 22px;
    margin-top: 20px;
    padding-left: 22px;
  }
  .headline, .contact-band {
    position: absolute;
    left: 0;
    top: 0;
    width: 725px;
    height: 994px;
  }
  .headline text, .phone-number {
    font-family: "Anton", sans-serif;
  }
</style>
</head>
<body>
  <div class="sign">
    <div class="brand-mark"></div>
    <h1 class="brand-name">Ridgeline Crest<span class="brand-sub">REALTY</span></h1>

    <svg class="headline" viewBox="0 0 725 994" aria-label="For Sale">
      <text x="59" y="616" font-size="276" fill="var(--sky-blue)" textLength="252" lengthAdjust="spacingAndGlyphs">FOR</text>
      <text x="340" y="616" font-size="276" fill="var(--brand-blue)" textLength="332" lengthAdjust="spacingAndGlyphs">SALE</text>
    </svg>

    <svg class="contact-band" viewBox="0 0 725 994">
      <rect class="ridge-area" x="0" y="770" width="725" height="224" fill="var(--navy)"
            role="img" aria-label="Mountain ridge silhouette"/>
      <circle cx="365" cy="751" r="53" fill="var(--navy)"/>
      <circle cx="365" cy="751" r="46" fill="var(--sign-white)"/>
      <g class="phone-icon" fill="none" stroke="var(--deep-blue)" stroke-linecap="round">
        <path d="M340 731 C335 735 336 745 344 757 C352 769 364 778 373 780 C377 781 381 778 383 775"
              stroke-width="10"/>
        <path d="M365 733 a14 14 0 0 1 14 14" stroke-width="3.5"/>
        <path d="M365 724 a23 23 0 0 1 23 23" stroke-width="3.5"/>
        <path d="M365 742 a5 5 0 0 1 5 5" stroke-width="3.5"/>
      </g>
      <text class="phone-number" x="84" y="930" font-size="108" fill="var(--sign-white)"
            textLength="562" lengthAdjust="spacingAndGlyphs">(555) 617 3489</text>
    </svg>
  </div>
</body>
</html>
```